TG - management consultant

Business card - contemporary design

Front info
Thomas Galloway

(Address not necessary)
PO Box 7324
Marlow Heights, CA 94088

(650) 482-3719
tg@thomasgallo.wy

Chirpline: tgq287
Friendwall: /Thomas.Galloway
Workhub: /in/thomasgalloway

Back or Front
www.thomasgalloway.net
Facilitation & coaching, change management, strategic partnerships, business improvement

Target Market(s)

High tech businesses - mostly startups in Silicon Valley

Industry/Entity Type

Business

Font styles to use
Sans Serif

Colors

Designer to choose colors to be used in the design.

```html
<!DOCTYPE html>
<html lang="en">
<head>
<meta charset="utf-8">
<title>Thomas Galloway – Business Card</title>
<link rel="stylesheet" href="https://fonts.googleapis.com/css2?family=Arimo:wght@700&family=Didact+Gothic&family=Poppins:ital,wght@1,700&family=PT+Sans+Narrow&display=swap">
<style>
  :root {
    --page: #e9e6e1;
    --ink: #1f1f1f;
    --black: #222222;
    --yellow: #f7f200;
    --orange: #fbb55e;
    --navy: #2e3192;
    --blue: #0f78c0;
    --white: #ffffff;
    --grey-dark: #4d4d4f;
    --grey-light: #dcdcdc;
    --grey-mid: #8a8a8c;
  }
  * { box-sizing: border-box; margin: 0; padding: 0; }
  html, body { width: 1200px; height: 900px; overflow: hidden; }
  body {
    background: var(--page);
    display: flex;
    flex-direction: column;
    align-items: center;
    justify-content: center;
    gap: 60px;
  }
  .card {
    position: relative;
    width: 560px;
    height: 320px;
    overflow: hidden;
    box-shadow: 0 6px 18px rgba(0,0,0,0.18);
  }
  .card-shapes { position: absolute; inset: 0; }

  /* Contact side */
  .contact-card { background: var(--orange); }
  .contact-name {
    position: absolute;
    left: 26px; top: 14px;
    font-family: "Poppins", sans-serif;
    font-weight: 700; font-style: italic;
    font-size: 44px;
    color: var(--yellow);
    letter-spacing: 0.5px;
    white-space: nowrap;
  }
  .contact-details {
    position: absolute;
    right: 22px; top: 108px;
    font-family: "Didact Gothic", sans-serif;
    font-size: 17px;
    line-height: 22px;
    color: var(--ink);
    text-align: right;
    white-space: nowrap;
  }
  .contact-details .address { margin-bottom: 18px; }
  .contact-phone, .contact-email {
    position: absolute;
    font-family: "Didact Gothic", sans-serif;
    font-size: 18px;
    color: var(--white);
    white-space: nowrap;
  }
  .contact-phone { left: 120px; top: 266px; }
  .contact-email { right: 24px; top: 287px; }

  /* Brand side */
  .brand-card {
    background: linear-gradient(135deg, var(--grey-dark) 0%, var(--grey-light) 45%, var(--grey-mid) 100%);
  }
  .brand-name {
    position: absolute;
    left: 118px; top: 70px;
    font-family: "Arimo", sans-serif;
    font-weight: 700;
    font-size: 46px;
    color: var(--yellow);
    white-space: nowrap;
  }
  .brand-url {
    position: absolute;
    left: 120px; top: 134px;
    font-family: "Didact Gothic", sans-serif;
    font-size: 26px;
    color: var(--white);
    white-space: nowrap;
  }
  .brand-services {
    position: absolute;
    left: 22px; top: 226px;
    font-family: "PT Sans Narrow", sans-serif;
    font-size: 18px;
    line-height: 22px;
    color: var(--white);
    white-space: nowrap;
  }
</style>
</head>
<body>

  <section class="card contact-card" aria-label="Card contact side">
    <svg class="card-shapes" width="560" height="320" viewBox="0 0 560 320" aria-hidden="true">
      <rect x="0" y="0" width="560" height="82" fill="var(--black)"/>
      <rect x="0" y="82" width="560" height="5" fill="var(--orange)"/>
      <rect x="0" y="87" width="560" height="3" fill="var(--black)"/>
      <polygon points="0,240 300,240 272,320 0,320" fill="var(--navy)"/>
      <polygon points="300,240 352,270 324,320 272,320" fill="var(--white)"/>
      <polygon points="352,270 560,270 560,320 324,320" fill="var(--blue)"/>
    </svg>
    <h1 class="contact-name">Thomas Galloway</h1>
    <div class="contact-details">
      <p class="address">PO Box 7324, Marlow Heights, CA 94088</p>
      <p>Chirpline: tgq287</p>
      <p>Friendwall: /Thomas.Galloway</p>
      <p>Workhub: /in/thomasgalloway</p>
    </div>
    <p class="contact-phone">(650) 482-3719</p>
    <p class="contact-email">tg@thomasgallo.wy</p>
  </section>

  <section class="card brand-card" aria-label="Card brand side">
    <svg class="card-shapes" width="560" height="320" viewBox="0 0 560 320" aria-hidden="true">
      <ellipse cx="280" cy="150" rx="330" ry="152" transform="rotate(-4 280 150)" fill="var(--black)"/>
    </svg>
    <h2 class="brand-name">Thomas Galloway</h2>
    <p class="brand-url">www.thomasgalloway.net</p>
    <p class="brand-services">Facilitation &amp; coaching, change management,<br>strategic partnerships, business improvement</p>
  </section>

</body>
</html>
```